New Crowdfunding site Fundlark needs banner ads

I’m looking for 4 standard size banner ads for www.fundlark.example to be used by LinkaDeal Affiliates in order to bring new crowdfunding projects to the platform.
728x90
160x600
300x250
180x160

Succesful designers will put on our Mentors list so that the project owner can also get their specific project banners from our designers. Designers can also become our affiliates either to promote Fundlark.example or individual projects.
Updates

Please note updated brief

Thank you to those that have submitted designs so far.
Please be reminded that the invitation will close tomorrow after which we will make our choice

Thanks for input so far.
Please note project closes tomorrow (Sunday) after which we will choose.

Target Market(s)

Target is a project owner with a project requiring $10,000 or more in any field including business and/or non-profits. Any country.
Inventors, creatives, communities, hardware or software, consumer items,

Industry/Entity Type

Crowdfunding

Font styles to use
Sans Serif

Requirements
Must have
• Clear button call to action based on our USPs shown on the home page but especially the use of Affiliate Networks to promote their project to the widest possible audience.

Text and button text should be editable (see png preference).
Call to action could be based on "Free Crowdfunding Consultation - is your project viable" or "Get Your Free Guide to Succesful Crowdfunding"
Nice to have
• .png format preferred with separate objects.
Some animation preferred in the button.

```html
<!DOCTYPE html>
<html lang="en">
<head>
<meta charset="utf-8">
<title>Fundlark banner ads</title>
<link rel="stylesheet" href="https://fonts.googleapis.com/css2?family=Michroma&family=Arimo:wght@400;700&display=swap">
<style>
  :root {
    --stage-light: #ffffff;
    --stage-dark: #bcbcbc;
    --panel-top: #ffffff;
    --panel-mid: #ebebeb;
    --panel-border: #c6c6c6;
    --brand-blue: #1515e0;
    --deep-blue: #1010c0;
    --brand-green: #38b21c;
    --band-green: #8cc63f;
    --band-green-dark: #77b52a;
    --button-green: #1f9a1a;
    --button-green-dark: #137a12;
    --play-dark: #3a4812;
    --play-light: #a8d64a;
    --white: #ffffff;
    --display: "Michroma", "Arial", sans-serif;
    --body: "Arimo", "Arial", sans-serif;
  }
  * { margin: 0; padding: 0; box-sizing: border-box; }
  html, body { width: 1200px; height: 1050px; overflow: hidden; }
  body {
    background: radial-gradient(ellipse 70% 60% at 50% 38%, var(--stage-light) 0%, #ececec 45%, var(--stage-dark) 100%);
    font-family: var(--body);
  }
  .stage { position: relative; width: 1200px; height: 1050px; }

  .banner {
    position: absolute;
    border: 1px solid var(--panel-border);
    overflow: hidden;
    background: linear-gradient(to bottom, var(--panel-top), #f2f2f2);
  }
  .banner > * { position: absolute; }
  .brand-mark {
    border-radius: 50%;
    background: var(--brand-blue);
  }
  .brand-name {
    font-family: var(--display);
    color: var(--brand-blue);
    line-height: 1;
    white-space: nowrap;
  }
  .tagline {
    font-family: var(--display);
    color: var(--brand-blue);
    line-height: 1;
    white-space: nowrap;
    text-align: center;
  }
  .tagline.is-green { color: var(--brand-green); }
  .band { left: 0; bottom: 0; display: block; }
  .band path { fill: var(--band-green); }

  /* Skyscraper 160x600 */
  .skyscraper { left: 70px; top: 87px; width: 242px; height: 902px; }
  .skyscraper .logo-area {
    left: 0; top: 0; width: 100%; height: 216px;
    background: linear-gradient(to bottom, #fafafa, var(--panel-mid));
  }
  .skyscraper .brand-mark { left: 84px; top: 66px; width: 74px; height: 74px; }
  .skyscraper .brand-name { left: 0; width: 100%; text-align: center; top: 272px; font-size: 28px; }
  .skyscraper .tagline { left: 0; width: 100%; font-size: 21px; }
  .skyscraper .line-project { top: 346px; }
  .skyscraper .line-plus { top: 404px; }
  .skyscraper .line-crowd { top: 463px; }
  .skyscraper .line-equals { top: 526px; }
  .skyscraper .line-funding { top: 586px; font-size: 27px; }
  .skyscraper .offer {
    left: 0; width: 100%; top: 720px;
    text-align: center; color: var(--white);
    font-family: var(--body); font-weight: 700;
    font-size: 21px; line-height: 44px;
  }
  .skyscraper .cta-button {
    left: 22px; top: 855px; width: 198px; height: 33px;
    border-radius: 4px;
    background: linear-gradient(to bottom, #2cb126, var(--button-green) 55%, var(--button-green-dark));
    box-shadow: 0 1px 2px rgba(0,0,0,0.3);
    color: var(--white); font-weight: 700; font-size: 15px;
    display: flex; align-items: center; justify-content: center; gap: 5px;
  }
  .cta-button .arrow { width: 0; height: 0; border-left: 5px solid var(--white); border-top: 4px solid transparent; border-bottom: 4px solid transparent; }

  /* Medium rectangle 300x250 */
  .rectangle { left: 391px; top: 388px; width: 454px; height: 377px; }
  .rectangle .brand-mark { left: 48px; top: 62px; width: 76px; height: 76px; }
  .rectangle .brand-name { left: 156px; top: 30px; font-size: 32px; }
  .rectangle .tagline { left: 170px; width: 276px; }
  .rectangle .line-pair { top: 104px; font-size: 21px; }
  .rectangle .line-result { top: 137px; font-size: 27px; }
  .rectangle .offer {
    left: 100px; width: 356px; top: 208px;
    text-align: center; color: var(--deep-blue);
    font-weight: 700; font-size: 24px; line-height: 29px;
  }
  .rectangle .offer .highlight { color: var(--brand-green); }
  .rectangle .cta-label {
    left: 36px; top: 317px;
    color: var(--white); font-size: 30px; line-height: 1;
    letter-spacing: 0.2px;
  }
  .rectangle .cta-play { left: 373px; top: 307px; width: 56px; height: 56px; }
</style>
</head>
<body>
<main class="stage">

  <section class="banner skyscraper" aria-label="Fundlark 160 by 600 banner">
    <div class="logo-area"></div>
    <div class="brand-mark" aria-hidden="true"></div>
    <div class="brand-name">Fundlark</div>
    <div class="tagline line-project">Project</div>
    <div class="tagline line-plus">+</div>
    <div class="tagline line-crowd">Crowd</div>
    <div class="tagline is-green line-equals">=</div>
    <div class="tagline is-green line-funding">Funding</div>
    <svg class="band" width="242" height="232" viewBox="0 0 242 232" aria-hidden="true">
      <path d="M0 35 H34 L50 3 Q52.5 -1 55 3 L71 35 H242 V232 H0 Z"/>
    </svg>
    <p class="offer">Get Your Free<br>Guide to Succesful<br>Crowdfunding</p>
    <a class="cta-button">GET STARTED NOW <span class="arrow"></span></a>
  </section>

  <section class="banner rectangle" aria-label="Fundlark 300 by 250 banner">
    <div class="brand-mark" aria-hidden="true"></div>
    <div class="brand-name">Fundlark</div>
    <div class="tagline line-pair">Project + Crowd</div>
    <div class="tagline is-green line-result">= Funding</div>
    <p class="offer">Get Your <span class="highlight">FREE</span> Guide to<br>Succesful Crowdfunding</p>
    <svg class="band" width="454" height="124" viewBox="0 0 454 124" aria-hidden="true">
      <path d="M0 38 H70 L86 3 Q88.5 -1 91 3 L107 38 H454 V124 H0 Z"/>
    </svg>
    <a class="cta-label">GET STARTED NOW</a>
    <svg class="cta-play" viewBox="0 0 56 56" aria-hidden="true">
      <circle cx="28" cy="28" r="27" fill="var(--play-dark)"/>
      <path d="M22 17 L38 28 L22 39 Z" fill="var(--play-light)"/>
    </svg>
  </section>

</main>
</body>
</html>
```